BOLD & MINIMALIST DESIGN NEEDED

We want a very bold but minimalistic business card design that is impactful and utilizes both sides of the business card. Our current logo is included for your use.

We want bold fonts and good use of negative space. We don't want the logo to overpower the design.

Target Market(s)

Professionals who are building new commercial buildings.

Industry/Entity Type

Construction

Contact Information for Business Card

Name, Title, email, office phone, cell phone, website

Font styles to use
Serif
Sans Serif

Requirements
Must have
• Bold design!

```html
<!DOCTYPE html>
<html lang="en">
<head>
<meta charset="utf-8">
<title>Crestline Business Card</title>
<link href="https://fonts.googleapis.com/css2?family=Montserrat:wght@500;600;700;800&display=swap" rel="stylesheet">
<style>
  :root {
    --backdrop: #d9dadc;
    --paper: #ffffff;
    --ink: #000000;
  }
  * { margin: 0; padding: 0; box-sizing: border-box; }
  html, body {
    width: 1200px;
    height: 900px;
    overflow: hidden;
    background: var(--backdrop);
    font-family: "Montserrat", sans-serif;
    color: var(--ink);
  }
  .canvas {
    position: relative;
    width: 1200px;
    height: 900px;
  }
  .card {
    position: absolute;
    width: 293px;
    height: 512px;
    background: var(--paper);
    overflow: hidden;
  }
  .card--front { left: 261px; top: 118px; }
  .card--back  { left: 647px; top: 271px; }

  /* Front */
  .front-base {
    position: absolute;
    left: 0; right: 0; bottom: 0;
    height: 140px;
    background: var(--ink);
  }
  .brand-name {
    position: absolute;
    left: 0; right: 0;
    top: 328px;
    text-align: center;
    font-weight: 800;
    font-size: 36px;
    letter-spacing: 0.5px;
    line-height: 1;
    color: var(--ink);
  }

  /* Back */
  .back-band {
    position: absolute;
    left: 0; right: 0; top: 0;
    height: 135px;
    background: var(--ink);
    display: flex;
    align-items: center;
    justify-content: center;
  }
  .band-name {
    color: var(--paper);
    font-weight: 800;
    font-size: 20px;
    letter-spacing: 1px;
  }
  .person-name {
    position: absolute;
    left: 0; right: 0; top: 158px;
    text-align: center;
    font-weight: 700;
    font-size: 26px;
    letter-spacing: 1.5px;
  }
  .person-title {
    position: absolute;
    left: 0; right: 0; top: 197px;
    text-align: center;
    font-weight: 600;
    font-size: 12.5px;
    letter-spacing: 1px;
  }
  .contact-list {
    position: absolute;
    left: 0; right: 0; top: 379px;
    list-style: none;
    text-align: center;
    font-weight: 500;
    font-size: 12px;
    letter-spacing: 1px;
    line-height: 18px;
  }
  .contact-label { margin-right: 8px; }
  .website {
    position: absolute;
    left: 0; right: 0; top: 453px;
    text-align: center;
    font-weight: 600;
    font-size: 12px;
    letter-spacing: 1px;
  }
</style>
</head>
<body>
<main class="canvas">
  <section class="card card--front" aria-label="Card front">
    <div class="brand-name">CRESTLINE</div>
    <div class="front-base"></div>
  </section>

  <section class="card card--back" aria-label="Card back">
    <div class="back-band"><span class="band-name">CRESTLINE</span></div>
    <h1 class="person-name">DANA REYES</h1>
    <p class="person-title">PROJECT MANAGER</p>
    <ul class="contact-list">
      <li><span class="contact-label">E :</span>+1 (555) 018-4420</li>
      <li><span class="contact-label">P :</span>+6019 7702 3148</li>
      <li><span class="contact-label">M :</span>DANA@CRESTLINE.COM</li>
    </ul>
    <p class="website">WWW.CRESTLINE.COM</p>
  </section>
</main>
</body>
</html>
```